Business Card for a Wedding Films Business

We require a business card design for our business 'Lewis Marrow Wedding Films'. The logo needs to look classy and high end.

Target Market(s)

Wedding Couples

Contact Information for Business Card

Lewis Marrow Wedding Films
07312 605 227
films@lewismarrowreels.com
www.lewismarrowreels.com

Facebook: @lewismarrowweddingfilms
Instagram: @lewismarrowfilms

Font styles to use
Sans Serif

Requirements
Must have
• Social media icons - Facebook and Instagram

```html
<!DOCTYPE html>
<html lang="en">
<head>
<meta charset="utf-8">
<title>Lewis Marrow Wedding Films – Business Card</title>
<link rel="stylesheet" href="https://fonts.googleapis.com/css2?family=Jost:wght@400;500&family=Open+Sans:wght@300;400&display=swap">
<style>
  :root {
    --backdrop: #8c8c8c;
    --card: #2a2a2a;
    --card-edge: #1e1e1e;
    --silver: #d4d4d4;
    --text: #e2e2e2;
    --muted: #bdbdbd;
    --icon-bg: #d8d8d8;
    --icon-fg: #2a2a2a;
    --emboss: #353535;
  }
  html, body {
    margin: 0;
    padding: 0;
    width: 1200px;
    height: 960px;
    overflow: hidden;
    background: var(--backdrop);
  }
  .canvas {
    position: relative;
    width: 1200px;
    height: 960px;
  }
  .card {
    position: absolute;
    top: 160px;
    width: 366px;
    height: 642px;
    border-radius: 18px;
    background: var(--card);
    box-shadow: 0 2px 0 var(--card-edge);
    overflow: hidden;
  }
  .card--front { left: 165px; }
  .card--back { left: 634px; }

  .wordmark {
    position: absolute;
    left: 0;
    right: 0;
    top: 345px;
    text-align: center;
    font-family: "Jost", sans-serif;
    font-weight: 400;
    color: var(--silver);
  }
  .wordmark__name {
    font-size: 27px;
    letter-spacing: 0.17em;
    line-height: 1;
    margin-left: 0.17em;
  }
  .wordmark__tagline {
    margin-top: 10px;
    font-size: 13px;
    letter-spacing: 0.34em;
    margin-left: 0.34em;
  }

  .contact-icons {
    position: absolute;
    top: 57px;
    left: 0;
    right: 0;
    display: flex;
    justify-content: center;
    gap: 10px;
  }
  .contact-icon {
    width: 20px;
    height: 20px;
    border-radius: 50%;
    background: var(--icon-bg);
    display: flex;
    align-items: center;
    justify-content: center;
  }
  .contact-list {
    position: absolute;
    top: 98px;
    left: 0;
    right: 0;
    text-align: center;
    font-family: "Open Sans", sans-serif;
    font-weight: 300;
    font-size: 17px;
    line-height: 26.5px;
    color: var(--text);
  }
  .divider {
    position: absolute;
    top: 205px;
    left: 153px;
    width: 60px;
    height: 2px;
    background: var(--text);
  }
  .social-list {
    position: absolute;
    top: 233px;
    left: 0;
    right: 0;
    text-align: center;
    font-family: "Open Sans", sans-serif;
    font-weight: 300;
    font-size: 17px;
    line-height: 27px;
    color: var(--text);
  }
  .social-item::before {
    content: "";
    display: inline-block;
    width: 12px;
    height: 12px;
    border-radius: 2px;
    background: var(--text);
    margin-right: 6px;
    vertical-align: -1px;
  }
  .back-name {
    position: absolute;
    right: 22px;
    bottom: 30px;
    font-family: "Jost", sans-serif;
    font-weight: 500;
    font-size: 40px;
    letter-spacing: 0.08em;
    line-height: 1.05;
    text-align: right;
    color: var(--emboss);
  }
</style>
</head>
<body>
<main class="canvas">
  <section class="card card--front" aria-label="Card front">
    <div class="wordmark">
      <div class="wordmark__name">LEWIS MARROW</div>
      <div class="wordmark__tagline">WEDDING FILMS</div>
    </div>
  </section>

  <section class="card card--back" aria-label="Card back">
    <div class="contact-icons">
      <span class="contact-icon" aria-label="Phone">
        <svg width="12" height="12" viewBox="0 0 24 24"><path fill="var(--icon-fg)" d="M6.6 10.8a15 15 0 0 0 6.6 6.6l2.2-2.2c.3-.3.7-.4 1-.2 1.1.4 2.3.6 3.6.6.6 0 1 .4 1 1V20c0 .6-.4 1-1 1A17 17 0 0 1 3 4c0-.6.4-1 1-1h3.5c.6 0 1 .4 1 1 0 1.3.2 2.5.6 3.6.1.3 0 .7-.2 1z"/></svg>
      </span>
      <span class="contact-icon" aria-label="Email">
        <svg width="12" height="12" viewBox="0 0 24 24"><rect x="2" y="5" width="20" height="14" rx="2" fill="var(--icon-fg)"/><path d="M3 6l9 7 9-7" fill="none" stroke="var(--icon-bg)" stroke-width="2"/></svg>
      </span>
      <span class="contact-icon" aria-label="Website">
        <svg width="12" height="12" viewBox="0 0 24 24" fill="none" stroke="var(--icon-fg)" stroke-width="2"><circle cx="12" cy="12" r="9"/><ellipse cx="12" cy="12" rx="4" ry="9"/><path d="M3 12h18"/></svg>
      </span>
    </div>
    <div class="contact-list">
      <div class="contact-phone">07312 605 227</div>
      <div class="contact-email">films@lewismarrowreels.com</div>
      <div class="contact-web">www.lewismarrowreels.com</div>
    </div>
    <div class="divider"></div>
    <div class="social-list">
      <div class="social-item">@lewismarrowweddingfilms</div>
      <div class="social-item">@lewismarrowfilms</div>
    </div>
    <div class="back-name">LEWIS<br>MARROW</div>
  </section>
</main>
</body>
</html>
```